Business Card Design for Varnel

I've already got the logo, but I'd like to see some interesting designs.

I don't want anything to complex. I like it simple,yet innovative, like the logo.

My business is System Administration for small to medium size businesses, so that will be my main target audience.
Updates

hey all, the png has been uploaded.

Hey all,

If you are submitting the back side of the card, I'd like the top bit of the card to be Varnel Solutions and the logo, the bottom of the card the website, with a white background.

The middle I'd like to leave blank for a quote that will be printed on each card.

Thanks!

Doug

Industry/Entity Type

Business

```html
<!DOCTYPE html>
<html lang="en">
<head>
<meta charset="utf-8">
<title>Varnel Solutions – Business Card</title>
<link rel="stylesheet" href="https://fonts.googleapis.com/css2?family=Fredoka:wght@600&family=Open+Sans:wght@600;700&display=swap">
<style>
  :root {
    --card-yellow: #fdc454;
    --brand-blue: #2775b2;
    --petal-top: #4a8fae;
    --petal-mid: #3aa2c7;
    --petal-bottom: #1697d6;
    --name-white: #ffffff;
  }
  * { margin: 0; padding: 0; box-sizing: border-box; }
  html, body {
    width: 1200px;
    height: 734px;
    overflow: hidden;
    background: var(--card-yellow);
  }
  .card {
    position: relative;
    width: 1200px;
    height: 734px;
    background: var(--card-yellow);
    overflow: hidden;
    font-family: "Open Sans", "Segoe UI", sans-serif;
  }
  .flower-area {
    position: absolute;
    inset: 0;
    width: 1200px;
    height: 734px;
  }
  .brand-mark {
    position: absolute;
    left: 0;
    top: 0;
    width: 300px;
    height: 734px;
  }
  .brand-name {
    position: absolute;
    left: 152px;
    top: 240px;
    transform: translate(-50%, -50%) rotate(-90deg);
    white-space: nowrap;
    font-family: "Open Sans", "Segoe UI", sans-serif;
    font-weight: 700;
    font-size: 50px;
    line-height: 1;
    color: var(--brand-blue);
  }
  .brand-dot {
    position: absolute;
    left: 42px;
    top: 482px;
    width: 220px;
    height: 220px;
    border-radius: 50%;
    background: var(--brand-blue);
  }
  .holder-name {
    position: absolute;
    left: 328px;
    top: 153px;
    font-family: "Fredoka", "Baloo 2", sans-serif;
    font-weight: 600;
    font-size: 70px;
    line-height: 1;
    color: var(--name-white);
    white-space: nowrap;
  }
  .holder-role {
    position: absolute;
    left: 352px;
    top: 235px;
    font-weight: 700;
    font-size: 46px;
    line-height: 1;
    color: var(--brand-blue);
    white-space: nowrap;
  }
  .contact-list {
    list-style: none;
    color: var(--brand-blue);
    font-weight: 700;
    font-size: 46px;
    line-height: 1;
  }
  .contact-list li {
    position: absolute;
    white-space: nowrap;
  }
  .contact-phone { left: 352px; top: 385px; }
  .contact-email { left: 356px; top: 464px; }
  .contact-web { left: 356px; top: 554px; }
</style>
</head>
<body>
  <main class="card">
    <svg class="flower-area" viewBox="0 0 1200 734" role="img" aria-label="Large blue flower illustration in the right corner">
      <defs>
        <linearGradient id="flower-fill" x1="0" y1="0" x2="0" y2="1">
          <stop offset="0" stop-color="#4a8fae"/>
          <stop offset="0.5" stop-color="#3aa2c7"/>
          <stop offset="1" stop-color="#1697d6"/>
        </linearGradient>
      </defs>
      <path d="M610 734 C700 560 820 470 900 400 C970 330 990 180 1090 0 L1200 0 L1200 734 Z" fill="url(#flower-fill)"/>
    </svg>

    <div class="brand-mark">
      <span class="brand-name">Varnel Solutions</span>
      <span class="brand-dot"></span>
    </div>

    <h1 class="holder-name">Name Here</h1>
    <p class="holder-role">System Administration</p>

    <ul class="contact-list">
      <li class="contact-phone">Telephone</li>
      <li class="contact-email">Email</li>
      <li class="contact-web">Website</li>
    </ul>
  </main>
</body>
</html>
```